Business Card Design Project

Roofing Consultant firm needs business card design

R.T. Falkner & Co., Inc
Roofing Consultants and Contractors
Specializing in Construction Defect Litigation

4817 Willow Bend Ct.
San Diego, CA 92340
Licences:
CA 503274, AZ 927416, NV 0081532
www.rtfalkner-example.com

Will need cards for 3 persons:
Robert T. Falkner - Principal Consultant
Gordon Bleake - Associate Expert
Tessa Varnum - Controller
ph-555-274-1600
fax -555-274-1602
Cell - (will be 3 different numbers)
Email - (will be 3 different addresses)
Attached graphic is what we had before..the RTF with the roof graphic has been our logo for awhile, but we are open to change.
Updates

I now see we will need to add an email field to the design.  Sorry I didnt think of it when I was setting this up.  Thank you for your submittals. They are all very good. 

Target Market(s)

Attorneys, Homeowner Associations, Insurance Carriers

Industry/Entity Type

Business

Requirements
Must have
• RTF logo roof design. (owner created)

```html
<!DOCTYPE html>
<html lang="en">
<head>
<meta charset="utf-8">
<title>R.T. Falkner &amp; Co., Inc — Business Card</title>
<link rel="stylesheet" href="https://fonts.googleapis.com/css2?family=Arimo:wght@400;700&family=Cabin:wght@400;500&display=swap">
<style>
  :root {
    --ink: #141414;
    --ink-soft: #333333;
    --roof-blue: #2a82c4;
    --paper-light: #ffffff;
    --paper-edge: #e9e9e9;
  }
  html, body {
    margin: 0;
    padding: 0;
    width: 1200px;
    height: 686px;
    overflow: hidden;
  }
  .card {
    position: relative;
    width: 1200px;
    height: 686px;
    background: radial-gradient(ellipse at 55% 40%, var(--paper-light) 0%, var(--paper-light) 45%, var(--paper-edge) 100%);
    font-family: "Arimo", Arial, sans-serif;
    color: var(--ink);
  }
  .brand {
    position: absolute;
    left: 20px;
    top: 100px;
    width: 560px;
  }
  .brand-mark-row {
    display: flex;
    align-items: flex-end;
    gap: 10px;
  }
  .brand-mark {
    width: 340px;
    height: 340px;
    background: var(--roof-blue);
  }
  .brand-suffix {
    margin: 0;
    font-size: 15px;
    font-weight: 700;
    line-height: 1.1;
  }
  .brand-name {
    margin: 22px 0 0;
    font-size: 70px;
    font-weight: 700;
    line-height: 1;
    letter-spacing: -1px;
  }
  .brand-tagline {
    margin: 14px 0 0;
    font-family: "Cabin", "Gill Sans", sans-serif;
    font-size: 28px;
    font-weight: 500;
    line-height: 1.1;
  }
  .brand-specialty {
    margin: 8px 0 0;
    font-family: "Cabin", "Gill Sans", sans-serif;
    font-size: 20px;
    font-weight: 400;
    color: var(--ink-soft);
  }
  .contact {
    position: absolute;
    right: 28px;
    top: 128px;
    text-align: right;
    font-size: 60px;
    font-weight: 700;
    line-height: 76px;
    letter-spacing: -0.5px;
  }
  .contact p { margin: 0; }
  .details {
    position: absolute;
    right: 28px;
    top: 530px;
    text-align: right;
    font-size: 22px;
    font-weight: 400;
    line-height: 30px;
    color: var(--ink-soft);
  }
  .details p { margin: 0; }
</style>
</head>
<body>
  <main class="card">
    <section class="brand">
      <div class="brand-mark-row">
        <div class="brand-mark" aria-hidden="true"></div>
        <p class="brand-suffix">&amp; Co.,<br>Inc</p>
      </div>
      <h1 class="brand-name">R.T. Falkner</h1>
      <p class="brand-tagline">Roofing Consultants &amp; Contractors</p>
      <p class="brand-specialty">Specializing in Construction Defect Litigation</p>
    </section>
    <section class="contact">
      <p class="contact-name">Robert T. Falkner</p>
      <p class="contact-title">Principal Consultant</p>
      <p class="contact-phone">Phone: 555 274 1600</p>
      <p class="contact-fax">Fax: 555 274 1602</p>
      <p class="contact-cell">Cell: 000 000 0000</p>
    </section>
    <section class="details">
      <p class="details-email">robert@rtfalkner-example.com</p>
      <p class="details-address">4817 Willow Bend Ct., San Diego, CA 92340</p>
      <p class="details-licences">Lic. CA 503274 · AZ 927416 · NV 0081532</p>
      <p class="details-web">www.rtfalkner-example.com</p>
    </section>
  </main>
</body>
</html>
```